Brochure Design Project

TGRP
The brochure is intended to be on Tarlow Guild of Restorative Practice website available for the members to download for the purpose of educating public about benefits of clinical hypnosis and introduce it as possible treatment option. There should be a empty space left on the last page for the member to stamp their office information.
So, the intended audience is general public that might be interested in hypnosis treatment
White on blue is logo of TGRP.
I would like the brochure to have bright complimentary colors with imagery that is used in health care/complimentary medicine - nature, relaxation, etc.
TGRP website is TGRPx.net.

```html
<!DOCTYPE html>
<html lang="en">
<head>
<meta charset="utf-8">
<title>TGRP Hypnosis Brochure</title>
<link rel="stylesheet" href="https://fonts.googleapis.com/css2?family=Source+Sans+3:ital,wght@0,300;0,400;0,600;0,700;1,400&display=swap">
<style>
  :root {
    --navy: #1a1a7e;
    --navy-deep: #12126a;
    --paper: #ffffff;
    --ink: #2b2b3a;
    --stage: #d9d9d9;
    --rule: #1a1a7e;
  }
  * { box-sizing: border-box; margin: 0; padding: 0; }
  html, body { width: 1200px; height: 800px; overflow: hidden; }
  body {
    background: var(--stage);
    font-family: "Source Sans 3", sans-serif;
    color: var(--ink);
    position: relative;
  }

  /* ---------- inside spread ---------- */
  .inside-sheet {
    position: absolute; left: 30px; top: 24px;
    width: 650px; height: 752px;
    background: var(--paper);
    display: grid;
    grid-template-rows: 262px 240px 250px;
  }

  /* top panel */
  .panel-why { display: grid; grid-template-columns: 420px 230px; position: relative; }
  .why-copy { padding: 16px 20px 36px 26px; position: relative; border-right: 5px solid var(--rule); }
  .section-label {
    display: inline-block; background: var(--navy); color: #fff;
    font-weight: 700; font-size: 12px; letter-spacing: .3px;
    padding: 3px 28px 3px 10px; text-transform: uppercase;
  }
  .bullet-list { list-style: none; margin-top: 8px; }
  .bullet-list li {
    font-size: 10px; line-height: 1.3; padding-left: 12px; position: relative; margin-bottom: 2px;
  }
  .bullet-list li::before { content: "•"; position: absolute; left: 2px; color: var(--navy); }
  .url-tab {
    position: absolute; background: var(--navy); color: #fff;
    font-size: 9.5px; font-weight: 600; padding: 3px 18px;
  }
  .why-copy .url-tab { left: 0; bottom: 8px; }
  .photo { position: relative; }
  .photo-reclining { background: linear-gradient(160deg, #f2f0ee 0%, #d9d2cc 45%, #c9a99a 70%, #5a4c48 100%); }

  .brand-mark {
    position: absolute; display: flex; align-items: center; gap: 6px;
    color: var(--navy); font-weight: 700;
  }
  .brand-mark .brand-square { width: 10px; height: 10px; background: var(--navy); flex: none; }
  .brand-mark .brand-name { font-size: 18px; line-height: 1; }
  .brand-mark .brand-full { display: block; font-size: 8px; line-height: 1.1; margin-top: 2px; text-transform: uppercase; }
  .panel-why .brand-mark { right: 12px; top: 18px; width: 128px; }

  /* middle panel */
  .panel-when { position: relative; display: grid; grid-template-columns: 180px 170px 150px 150px; }
  .photo-stress { background: linear-gradient(150deg, #f3f1ee 0%, #d8cbc2 50%, #6b4c3e 100%); }
  .photo-meditate { background: linear-gradient(170deg, #6f9a52 0%, #a9c486 40%, #b8c3dd 75%, #8d9fc6 100%); }
  .photo-class { background: linear-gradient(170deg, #efe6da 0%, #d8c2a8 55%, #b48d69 100%); }
  .photo-calm { background: linear-gradient(170deg, #e2d6c8 0%, #c7a58a 55%, #7d5a44 100%); }
  .when-band {
    position: absolute; left: 0; right: 0; bottom: 0; height: 62px; background: var(--navy);
  }
  .when-box {
    position: absolute; left: 150px; bottom: 16px; width: 310px;
    background: var(--navy-deep); border: 1.5px solid #fff; color: #fff;
    text-align: center; padding: 8px 14px 10px;
  }
  .when-box h3 { font-size: 13px; font-weight: 700; font-style: italic; }
  .when-box p { font-size: 10px; font-style: italic; line-height: 1.35; margin-top: 3px; }
  .when-url {
    position: absolute; left: 240px; bottom: 3px; color: #fff;
    font-size: 9px; letter-spacing: 4px;
  }

  /* bottom panel */
  .panel-right-for-me { display: grid; grid-template-columns: 220px 430px; position: relative; border-top: 6px solid var(--navy); }
  .photo-landscape { background: linear-gradient(180deg, #cfd6da 0%, #8ea1a8 35%, #5d7a58 65%, #3f5a2f 85%, #a59a3a 100%); }
  .panel-right-for-me .brand-mark { left: 12px; top: 12px; width: 150px; }
  .right-copy { padding: 16px 24px 36px 20px; position: relative; }
  .right-copy .bullet-list li { font-size: 10px; line-height: 1.3; margin-bottom: 2px; }
  .closing-note { font-size: 10px; line-height: 1.35; margin-top: 6px; font-style: italic; }
  .right-copy .url-tab { right: 0; bottom: 8px; }

  /* ---------- cover ---------- */
  .cover-sheet {
    position: absolute; left: 712px; top: 170px;
    width: 460px; height: 440px; background: var(--paper);
    display: grid; grid-template-columns: 262px 198px;
  }
  .cover-art {
    position: relative;
    background: radial-gradient(circle at 55% 40%, #f2e9ff 0%, #b596e6 14%, #5a54c9 38%, #26248f 70%, #0f0f55 100%);
  }
  .cover-art .url-tab { left: 0; bottom: 14px; font-size: 10px; padding: 4px 22px; }
  .cover-front { position: relative; border-left: 5px solid var(--rule); padding: 34px 14px 0 18px; }
  .cover-front .brand-mark { position: static; }
  .cover-front .brand-name { font-size: 30px; }
  .cover-front .brand-full { font-size: 10px; }
  .cover-title {
    margin-top: 34px; font-weight: 300; font-size: 34px; letter-spacing: .5px; color: var(--navy);
  }
  .question-box {
    position: absolute; left: 12px; right: 10px; top: 250px; height: 120px;
    border: 1.5px solid var(--navy); padding: 4px;
  }
  .question-box-inner {
    background: var(--navy); height: 100%; color: #fff; position: relative;
    padding: 12px 0 0 16px; font-size: 11.5px; font-style: italic; line-height: 1.3;
  }
  .question-icon {
    position: absolute; right: 10px; top: 8px; width: 44px; height: 44px; border-radius: 50%;
    background: radial-gradient(circle, #ffffff 0%, #e8e8ee 55%, #c9c9d6 100%);
    border: 1.5px solid #fff;
  }
</style>
</head>
<body>

<section class="inside-sheet" aria-label="Brochure inside spread">

  <div class="panel-why">
    <div class="why-copy">
      <h2 class="section-label">Why use hypnosis</h2>
      <ul class="bullet-list">
        <li>Hypnosis is unique in its ability to help you unlock imagination, bypass the “can never happen” censor of the conscious mind, and simply help one see experiences and memories in a different light.</li>
        <li>It can help find solutions and resolutions to a difficult mental or physical problem, and find inner sources of strength and resilience.</li>
        <li>It can help a person better understand one’s own as well as others’ motivations and behavior.</li>
        <li>It allows a person to choose and develop abilities and capacities that can help achieve a desired goal.</li>
        <li>During the process of hypnosis a person is frequently taught how use individualized cues and techniques to achieve desired result (decrease anxiety, reduce pain, improve sport performance, etc.) With practice, a person can achieve a level of control that seemed impossible before.</li>
      </ul>
      <span class="url-tab">www.tgrpx.net</span>
    </div>
    <div class="photo photo-reclining" role="img" aria-label="Photo of a woman resting with closed eyes on a sofa while a therapist takes notes">
      <div class="brand-mark">
        <span class="brand-square"></span>
        <span><span class="brand-name">TGRP</span><span class="brand-full">Tarlow Guild of Restorative Practice</span></span>
      </div>
    </div>
  </div>

  <div class="panel-when">
    <div class="photo photo-stress" role="img" aria-label="Photo of a stressed woman holding her head"></div>
    <div class="photo photo-meditate" role="img" aria-label="Photo of a woman meditating outdoors among greenery"></div>
    <div class="photo photo-class" role="img" aria-label="Photo of a group meditating in a bright room"></div>
    <div class="photo photo-calm" role="img" aria-label="Photo of a man meditating with closed eyes"></div>
    <div class="when-band"></div>
    <div class="when-box">
      <h3>When</h3>
      <p>Hypnosis has been found to be very effective for treating many mental and physical conditions, as well improving physical and mental performance, and changing undesirable habits.</p>
    </div>
    <span class="when-url">www.tgrpx.net</span>
  </div>

  <div class="panel-right-for-me">
    <div class="photo photo-landscape" role="img" aria-label="Photo of a misty green mountain valley with a rainbow">
      <div class="brand-mark">
        <span class="brand-square"></span>
        <span><span class="brand-name">TGRP</span><span class="brand-full">Tarlow Guild of Restorative Practice</span></span>
      </div>
    </div>
    <div class="right-copy">
      <h2 class="section-label">Is hypnosis right for me?</h2>
      <ul class="bullet-list">
        <li>Hypnosis is a wonderful and effective tool. If you are not familiar with hypnosis, you might worry about loss of control and wonder if your problems can be helped.</li>
        <li>Hypnosis might offer a novel way to approach or resolve the problem, or just see it in a different light.</li>
        <li>Even if hypnosis does not immediately solve the problem, you can still learn how to be a little more comfortable and experience a deeper level of physical and mental relaxation.</li>
        <li>Well trained medical or mental health professionals will help you discover and use resources and strengths that you did not know you had.</li>
      </ul>
      <p class="closing-note">Your therapist, doctor or dentist might be the best person to discuss hypnosis and how it can be helpful to you. Licensed professionals get their training and certification through the Tarlow Guild of Restorative Practice. You can find a list of certified providers on TGRPx.net.</p>
      <span class="url-tab">www.tgrpx.net</span>
    </div>
  </div>

</section>

<section class="cover-sheet" aria-label="Brochure front cover">
  <div class="cover-art" role="img" aria-label="Illustration of a glowing human head with bright neural network points in blue and violet light">
    <span class="url-tab">www.tgrpx.net</span>
  </div>
  <div class="cover-front">
    <div class="brand-mark">
      <span class="brand-square"></span>
      <span><span class="brand-name">TGRP</span><span class="brand-full">Tarlow Guild of Restorative Practice</span></span>
    </div>
    <h1 class="cover-title">HYPNOSIS</h1>
    <div class="question-box">
      <div class="question-box-inner">
        What,<br>Why,<br>When,<br>How, and<br>Could it be right for me?
        <span class="question-icon" role="img" aria-label="Illustration of a figure beside a large question mark"></span>
      </div>
    </div>
  </div>
</section>

</body>
</html>
```